Kestrel & Dunmore Varnell Cargomax 2400

Need to create a wrap that really POPS. The customer is a home contractor. His website is https://kestreldunmore.com/
He wants the wrap to capture everything he creates. The work truck is a 2012 Varnell Cargomax box truck 3500. The box is 12ft wide x 86" tall. The rear door is 70" tall x 70" wide. He wants to incorporate red/gray/black into the logo and design. Also, he likes the attached wrap design. Use that for inspiration, please do not copy directly.

```html
<!DOCTYPE html>
<html lang="en">
<head>
<meta charset="utf-8">
<title>Kestrel &amp; Dunmore — Varnell Cargomax 2400 Wrap</title>
<link href="https://fonts.googleapis.com/css2?family=Montserrat:wght@600;700;800&display=swap" rel="stylesheet">
<style>
  :root {
    --ink: #121212;
    --paper: #ffffff;
    --panel: #f4f4f4;
    --maroon: #5b2a2d;
    --edge: #cfcfcf;
  }
  html, body {
    margin: 0;
    width: 900px;
    height: 1200px;
    overflow: hidden;
    background: var(--paper);
  }
  .wrap-sheet { display: block; width: 900px; height: 1200px; }
  .panel-base { fill: var(--panel); stroke: var(--edge); stroke-width: 1; }
  .panel-black { fill: var(--ink); }
  .stripe-maroon { fill: none; stroke: var(--maroon); stroke-width: 7; stroke-linejoin: miter; }
  .band-maroon { fill: var(--maroon); }
  .brand-name { font-family: "Montserrat", sans-serif; font-weight: 800; fill: var(--maroon); text-anchor: middle; letter-spacing: 0.5px; }
  .brand-name--light { fill: var(--paper); }
  .service-line { font-family: "Montserrat", sans-serif; font-weight: 800; fill: var(--ink); text-anchor: middle; letter-spacing: 1px; }
  .service-line--light { fill: var(--paper); }
  .tagline { font-family: "Montserrat", sans-serif; font-weight: 700; fill: var(--ink); text-anchor: middle; letter-spacing: 0.6px; }
  .tagline--light { fill: var(--paper); }
  .contact-phone { font-family: "Montserrat", sans-serif; font-weight: 600; fill: var(--paper); }
  .contact-url { font-family: "Montserrat", sans-serif; font-weight: 700; fill: var(--paper); }
  .phone-badge { fill: var(--paper); }
  .phone-glyph { fill: var(--ink); }
</style>
</head>
<body>
<svg class="wrap-sheet" viewBox="0 0 900 1200" xmlns="http://www.w3.org/2000/svg">
  <defs>
    <symbol id="phone-icon" viewBox="0 0 20 20">
      <circle class="phone-badge" cx="10" cy="10" r="10"/>
      <path class="phone-glyph" d="M6.2 4.6c.5-.3 1-.2 1.3.3l1.1 2c.2.4.1.9-.2 1.2l-.8.7c.6 1.4 1.6 2.5 3 3.2l.7-.8c.3-.3.8-.4 1.2-.2l2 1.1c.5.3.6.8.3 1.3l-.7 1.1c-.4.6-1.1.9-1.8.7-3.6-1-6.4-3.9-7.4-7.5-.2-.7.1-1.4.7-1.8z"/>
    </symbol>
  </defs>

  <!-- Driver side: cab door decal -->
  <g class="cab-door cab-door--driver" transform="translate(222,230)">
    <rect class="panel-base" width="124" height="100"/>
    <rect class="panel-black" y="64" width="124" height="36"/>
    <rect class="band-maroon" y="56" width="124" height="4"/>
    <text class="brand-name" x="62" y="28" font-size="10">KESTREL &amp; DUNMORE</text>
    <text class="service-line" x="62" y="41" font-size="8">REMODELING</text>
    <text class="tagline" x="62" y="50" font-size="4">KITCHEN | BATHROOM | HOME REPAIR</text>
  </g>

  <!-- Driver side: box panel -->
  <g class="box-side box-side--driver" transform="translate(350,63)">
    <rect class="panel-base" width="410" height="225"/>
    <polygon class="panel-black" points="81,225 168,147 285,147 410,63 410,225"/>
    <polyline class="stripe-maroon" points="38,225 160,139 280,139 410,52"/>
    <text class="brand-name" x="160" y="88" font-size="24">KESTREL &amp; DUNMORE</text>
    <text class="service-line" x="160" y="112" font-size="17">REMODELING</text>
    <text class="tagline" x="160" y="126" font-size="7.5">KITCHEN | BATHROOM | HOME REPAIR</text>
    <use href="#phone-icon" x="236" y="189" width="15" height="15" transform="translate(0,-24)"/>
    <text class="contact-phone" x="257" y="177" font-size="13">(555) 214-0386</text>
    <text class="contact-url" x="233" y="193" font-size="8.5">kestreldunmore.com</text>
  </g>

  <!-- Passenger side: box panel -->
  <g class="box-side box-side--passenger" transform="translate(141,453)">
    <rect class="panel-base" width="410" height="225"/>
    <g transform="translate(410,0) scale(-1,1)">
      <polygon class="panel-black" points="81,225 168,147 285,147 410,63 410,225"/>
      <polyline class="stripe-maroon" points="38,225 160,139 280,139 410,52"/>
    </g>
    <text class="brand-name" x="250" y="88" font-size="24">KESTREL &amp; DUNMORE</text>
    <text class="service-line" x="250" y="112" font-size="17">REMODELING</text>
    <text class="tagline" x="250" y="126" font-size="7.5">KITCHEN | BATHROOM | HOME REPAIR</text>
    <use href="#phone-icon" x="51" y="165" width="15" height="15"/>
    <text class="contact-phone" x="72" y="177" font-size="13">(555) 214-0386</text>
    <text class="contact-url" x="49" y="193" font-size="8.5">kestreldunmore.com</text>
  </g>

  <!-- Passenger side: cab door decal -->
  <g class="cab-door cab-door--passenger" transform="translate(555,618)">
    <rect class="panel-base" width="124" height="100"/>
    <rect class="panel-black" y="64" width="124" height="36"/>
    <rect class="band-maroon" y="56" width="124" height="4"/>
    <text class="brand-name" x="62" y="28" font-size="10">KESTREL &amp; DUNMORE</text>
    <text class="service-line" x="62" y="41" font-size="8">REMODELING</text>
    <text class="tagline" x="62" y="50" font-size="4">KITCHEN | BATHROOM | HOME REPAIR</text>
  </g>

  <!-- Rear roll door -->
  <g class="rear-door" transform="translate(288,837)">
    <rect class="panel-base" width="372" height="339"/>
    <rect class="band-maroon" y="68" width="372" height="8"/>
    <rect class="panel-black" y="81" width="372" height="258"/>
    <text class="brand-name brand-name--light" x="186" y="152" font-size="20">KESTREL &amp; DUNMORE</text>
    <text class="service-line service-line--light" x="186" y="171" font-size="13">REMODELING</text>
    <text class="tagline tagline--light" x="186" y="181" font-size="5.5">KITCHEN | BATHROOM | HOME REPAIR</text>
    <use href="#phone-icon" x="80" y="212" width="26" height="26"/>
    <text class="contact-phone" x="114" y="233" font-size="22">(555) 214-0386</text>
    <text class="contact-url" x="186" y="258" font-size="14" text-anchor="middle">kestreldunmore.com</text>
  </g>
</svg>
</body>
</html>
```